Design for a Cell Phone Display Case

We are importing and distributing in Canada. The project will be in english but we will need to translate it into english. We have created a new cell case for our market. The beauty of the case is that it is UNIVERSAL. WHich mean almost all cell phone should fit on it. Just the big one such as Quorin 8 max is not fitting. Most of our models will be for 20-30 years old. We need you to design on the die cut file. If you need the AI ​​file, please ask, we can offer it. 1- The design of the display 2- Header (The most important) We need to make sure that the consumer will understand really fast what it is about. Some words but not too much. Title should be: Universal Cell Case Image 1: Cell Case 1 Main should be on the header. This image show well what it is about. Please do not use the text already on the picture. Please offer another way to express the functions. I really like the original ICONE to help to express. Image 2: Cell Case 2: This image should be smaller than Maybe it's in a bubble with an arrow to show what it is about. You guys decide. Our company sell colorful products. OUr cell case will be different colors and cool images. We think that maybe a good thing. We let you be creative. Final: We need to understand this cell case. Please feel free for any questions.
Updates

Reason: We did not get enough proposal ....

Target Market(s)

Consumer should be 20 to 35 years old

Industry/Entity Type

Cell Phone

Font styles to use
Serif

Colors
3277b5

Requirements
Must have
• Please remove the text on the image: Cell Case 1 - Main. I need you to explain the same thing. Image: Cell box 1 main need to be on the header. We really need to understand what it is and how it works. . . . . . . . . . . . . . . . . . . . . . . . . . . . . . . . . . . . . . . . . . . .
Nice to have
• I would like to use ICON to demonstrate the function. I would like to use ICON to demonstrate the function. I would like to use ICON to demonstrate the function. I would like to use ICON to demonstrate the function. I would like to use ICON to demonstrate the function. I would like to use ICON to demonstrate the function.
Should not have
• Not too much text on the HEADER. Not too much text on the HEADER.

```html
<!DOCTYPE html>
<html lang="en">
<head>
<meta charset="utf-8">
<title>Universal Cell Case</title>
<link rel="stylesheet" href="https://fonts.googleapis.com/css2?family=Russo+One&family=Raleway:wght@300;400&display=swap">
<style>
  :root {
    --bg-light: #fbfbfc;
    --bg-mid: #dcdde0;
    --bg-dark: #a9abb0;
    --red: #d4202a;
    --red-light: #f04048;
    --red-dark: #8e1016;
    --ink: #25262a;
    --case-black: #18191c;
    --case-grey: #45474d;
    --line: #55575c;
  }
  html, body {
    margin: 0;
    padding: 0;
    width: 1200px;
    height: 621px;
    overflow: hidden;
  }
  .banner {
    position: relative;
    width: 1200px;
    height: 621px;
    overflow: hidden;
    background: radial-gradient(ellipse 70% 80% at 45% 35%, var(--bg-light) 0%, var(--bg-mid) 60%, var(--bg-dark) 100%);
  }
  .banner > * { position: absolute; }
  .backdrop { left: 0; top: 0; }
  .title {
    right: 66px;
    top: 52px;
    margin: 0;
    text-align: right;
    font-weight: normal;
  }
  .title-main {
    display: block;
    font-family: "Russo One", sans-serif;
    font-size: 62px;
    line-height: 1;
    letter-spacing: 3px;
    background: linear-gradient(180deg, var(--red-light) 0%, var(--red) 55%, var(--red-dark) 100%);
    -webkit-background-clip: text;
    background-clip: text;
    -webkit-text-fill-color: transparent;
  }
  .title-sub {
    display: block;
    margin-top: 6px;
    font-family: "Raleway", sans-serif;
    font-weight: 300;
    font-size: 46px;
    line-height: 1;
    letter-spacing: 4px;
    color: var(--ink);
  }
  .product-main { left: 40px; top: 110px; }
  .product-range { left: 740px; top: 200px; }
  .icon-fit { left: 460px; top: 50px; }
  .size-scale { left: 460px; top: 140px; }
  .size-label {
    font-family: "Raleway", sans-serif;
    font-weight: 400;
    font-size: 9px;
    fill: var(--ink);
  }
  .detail-closed { left: 150px; top: 300px; }
</style>
</head>
<body>
<main class="banner">
  <svg class="backdrop" width="1200" height="621" viewBox="0 0 1200 621" aria-hidden="true">
    <defs>
      <radialGradient id="glow">
        <stop offset="0" stop-color="#ffffff" stop-opacity="1"/>
        <stop offset="1" stop-color="#ffffff" stop-opacity="0"/>
      </radialGradient>
      <linearGradient id="streak" x1="0" y1="0" x2="1" y2="0">
        <stop offset="0" stop-color="#ffffff" stop-opacity="0"/>
        <stop offset="0.5" stop-color="#ffffff" stop-opacity="0.8"/>
        <stop offset="1" stop-color="#ffffff" stop-opacity="0"/>
      </linearGradient>
    </defs>
    <circle cx="320" cy="40" r="190" fill="url(#glow)"/>
    <circle cx="840" cy="520" r="160" fill="url(#glow)"/>
    <circle cx="1130" cy="560" r="110" fill="url(#glow)"/>
    <polygon points="0,80 260,0 300,0 0,130" fill="url(#streak)" opacity="0.7"/>
    <polygon points="620,621 1200,380 1200,400 680,621" fill="url(#streak)" opacity="0.5"/>
  </svg>

  <h1 class="title">
    <span class="title-main">UNIVERSAL</span>
    <span class="title-sub">CELL CASE</span>
  </h1>

  <svg class="product-main" width="680" height="420" viewBox="0 0 680 420" role="img" aria-label="Open black carbon-texture wallet case with a clear window on the flap and an adjustable clip tray that grips phones of many widths">
    <defs>
      <linearGradient id="caseTone" x1="0" y1="0" x2="1" y2="1">
        <stop offset="0" stop-color="var(--case-grey)"/>
        <stop offset="0.55" stop-color="#2a2b2f"/>
        <stop offset="1" stop-color="var(--case-black)"/>
      </linearGradient>
    </defs>
    <path d="M22,222 L238,18 Q250,8 266,12 L648,112 Q664,118 656,134 L480,352 Q470,366 452,362 L30,250 Q12,242 22,222 Z" fill="url(#caseTone)"/>
  </svg>

  <svg class="icon-fit" width="180" height="100" viewBox="0 0 180 100" aria-hidden="true">
    <rect x="68" y="4" width="42" height="64" rx="6" fill="var(--case-black)"/>
    <rect x="72" y="12" width="34" height="46" fill="#ffffff"/>
    <rect x="60" y="24" width="8" height="26" fill="var(--case-grey)"/>
    <rect x="110" y="24" width="8" height="26" fill="var(--case-grey)"/>
    <polygon points="2,37 18,28 18,34 54,34 54,40 18,40 18,46" fill="var(--red)"/>
    <polygon points="178,37 162,28 162,34 126,34 126,40 162,40 162,46" fill="var(--red)"/>
  </svg>

  <svg class="size-scale" width="200" height="70" viewBox="0 0 200 70" aria-hidden="true">
    <line x1="12" y1="16" x2="190" y2="16" stroke="var(--line)" stroke-width="1"/>
    <line x1="12" y1="12" x2="12" y2="20" stroke="var(--line)"/>
    <line x1="100" y1="12" x2="100" y2="20" stroke="var(--line)"/>
    <line x1="190" y1="12" x2="190" y2="20" stroke="var(--line)"/>
    <text class="size-label" x="44" y="10">53mm</text>
    <text class="size-label" x="134" y="10">83mm</text>
    <line x1="100" y1="20" x2="100" y2="70" stroke="var(--line)" stroke-width="1"/>
  </svg>

  <svg class="detail-closed" width="140" height="300" viewBox="0 0 140 300" aria-hidden="true">
    <line x1="62" y1="172" x2="160" y2="110" stroke="var(--line)" stroke-width="1"/>
    <polygon points="42,140 32,154 39,154 39,174 45,174 45,154 52,154" fill="var(--red)"/>
    <rect x="26" y="180" width="34" height="98" rx="4" fill="var(--case-black)" role="img" aria-label="Closed black wallet case seen from the back, showing the camera opening"/>
    <polygon points="42,298 32,284 39,284 39,284 45,284 52,284" fill="var(--red)"/>
    <rect x="39" y="280" width="6" height="0" fill="var(--red)"/>
    <rect x="86" y="218" width="20" height="14" rx="2" fill="var(--red)"/>
    <rect x="92" y="215" width="8" height="4" fill="var(--red)"/>
    <circle cx="96" cy="225" r="4" fill="#ffffff"/>
    <circle cx="96" cy="225" r="2.2" fill="var(--red)"/>
  </svg>

  <svg class="product-range" width="440" height="320" viewBox="0 0 440 320" role="img" aria-label="Row of closed wallet cases standing in perspective, in black, brown, orange, blue, red, white and pink">
    <defs>
      <linearGradient id="rangeTone" x1="0" y1="0" x2="1" y2="0">
        <stop offset="0" stop-color="#1a1b1e"/>
        <stop offset="0.24" stop-color="#2a2b2f"/>
        <stop offset="0.24" stop-color="#6b4331"/>
        <stop offset="0.4" stop-color="#5a3526"/>
        <stop offset="0.4" stop-color="#e07020"/>
        <stop offset="0.52" stop-color="#c85e16"/>
        <stop offset="0.52" stop-color="#3a7fc0"/>
        <stop offset="0.64" stop-color="#2a66a6"/>
        <stop offset="0.64" stop-color="#d42630"/>
        <stop offset="0.76" stop-color="#b01a22"/>
        <stop offset="0.76" stop-color="#f4f4f4"/>
        <stop offset="0.87" stop-color="#dcdcdc"/>
        <stop offset="0.87" stop-color="#e0408a"/>
        <stop offset="1" stop-color="#c42c74"/>
      </linearGradient>
    </defs>
    <path d="M16,20 L420,92 L420,286 L16,310 Z" fill="url(#rangeTone)"/>
  </svg>
</main>
</body>
</html>
```